Residential Mortgage Leader needs Wordpress Design

Looking for a home page website design for a client. We develop using the WordPress platform and would prefer the design be at least loosely based on an existing WordPress template. Attached files have many notes from our creative brief with client. The site must be responsive. Approved, basic wireframe attached. There is room for interpretation.

Existing web site: http://www.marisolbrandt.example/

The Marisol Brandt Team relies on strong systems to deliver an on-time, done-right, friendly experience. Marisol offers mortgages and refinancing services throughout the United States. She is a successful Keystone Funding agent who strives to be an active part of her community. She would like to focus the site on her team, rather than just her.

Difference makers...
When you work with The Marisol Brandt Team you get a high level of expertise and a friendly experience.

She has amazing credentials. Marisol is widely recognized as a top producer for her company, and has earned a number of awards and honors for her customer service.

Marisol's team is very engaged and enjoys sharing social comments or photos from their community.

Imagery:
* Friendly, warm imagery, preferably of her team or an image to represent her team
* Clean and crisp
* Professional / Experts in mortgage and refinance
* Clean / Good use of white space
Updates

When possible, please use imagery from the DFW area. The client mentioned they would prefer not to see stock images. Thanks.

Amend that- creative use of stock images, however, is fine. A few designs have used stock imagery, but in a well-considered manner.

We added some photos and graphics that are local. We are Dallas / Ft. Worth, Plano, Frisco, Texas. We also added some examples of photos to use for the "In the Community" area. Stock photos of business folks just doesn't fit there. Thanks!

Target Market(s)

They service a lot of builders, but also work with homeowners. Their typical client is usually a woman searching for mortgage services online. She typically has a family and may refer her husband to Marisol's team. Keep in mind, however, they also see a number of other scenarios. Most of their clients are middle to high-end borrowers.

Industry/Entity Type

It Company

Requirements
Must have
• Design should be developed using program such as Photoshop or Fireworks or Illustrator as last preference. Ideally, the design would be based on an existing responsive WordPress theme, which we would customize. You must include the name of the target theme. The footer should include lots of space for disclaimers and legal language. Site navigation should include these choices: "Home, About, Builders, Mortgage Info, Approval, Blog, Contact"
Nice to have
• Blog, social media and photos area. Use of the already approved style prototype with colors and fonts (Lato- a Google font, Times New Roman and Cookie-a decorative Google font). However, we are open to interpretation.
Should not have
• Hard to read fonts or a lack of white space.

```html
<!DOCTYPE html>
<html lang="en">
<head>
<meta charset="utf-8">
<title>Marisol Brandt Team – Home</title>
<link rel="stylesheet" href="https://fonts.googleapis.com/css2?family=Lato:wght@400;700&family=Cinzel:wght@400&family=Cookie&display=swap">
<style>
:root{
  --red:#c0160f;
  --red-dark:#a3120b;
  --ink:#2b2b2b;
  --grey-text:#555;
  --grey-soft:#8c8c8c;
  --page:#f4f4f4;
  --header-bg:#efefef;
  --panel:#e6e5e3;
  --widget-dark:#3a3a3a;
  --widget-line:#4d4d4d;
  --green:#1f4d2a;
  --sky:#2a5df2;
  --fb-blue:#3b5998;
  --white:#fff;
}
*{box-sizing:border-box;margin:0;padding:0}
html,body{width:858px;height:1200px;overflow:hidden;background:var(--page)}
body{font-family:'Lato',Arial,sans-serif;color:var(--ink)}
h1,h2,h3{font-weight:400}
.canvas{position:relative;width:858px;height:1200px;overflow:hidden;background:var(--page)}

/* header */
.site-header{position:absolute;left:0;top:0;width:858px;height:120px;background:var(--header-bg)}
.brand{position:absolute;left:62px;top:26px}
.brand-name{font-family:'Lato',Arial,sans-serif;font-weight:400;font-size:44px;line-height:44px;color:var(--red);letter-spacing:-0.5px}
.brand-tag{font-size:13px;letter-spacing:1.6px;color:var(--grey-soft);margin-top:4px;padding-left:86px}
.work-tab{position:absolute;left:523px;top:0;width:257px;height:31px;background:#3c3c3c;border-radius:0 0 14px 14px;color:var(--white);display:flex;align-items:center;justify-content:center;gap:10px}
.work-tab .label{font-style:italic;font-weight:700;font-size:13px}
.work-tab .phone{font-weight:700;font-size:14px}
.header-mail{position:absolute;left:588px;top:39px;display:flex;align-items:center;gap:8px;font-size:13px;font-weight:700;color:#444}

/* nav */
.main-nav{position:absolute;left:0;top:120px;width:858px;height:34px;background:linear-gradient(#dd1c12,#b5120b)}
.main-nav a{position:absolute;top:10px;transform:translateX(-50%);color:var(--white);text-decoration:none;font-size:10.5px;font-weight:700;white-space:nowrap}

/* hero */
.hero-backdrop{position:absolute;left:0;top:154px;width:858px;height:303px;background:linear-gradient(#cfcfcf,#e9e9e9 60%,#f1f1f1)}
.hero-panel{position:absolute;left:55px;top:176px;width:717px;height:280px;background:var(--panel)}
.hero-photo{position:absolute;left:26px;top:22px;width:338px;height:239px;background:linear-gradient(160deg,#3b6cff,var(--sky));border:2px solid #4d7af0}
.hero-title{position:absolute;left:382px;top:18px;font-family:'Cinzel',Georgia,serif;font-weight:400;font-size:36px;line-height:36px;color:#2d2d2d;letter-spacing:1px}
.hero-text{position:absolute;left:382px;top:97px;width:318px;font-size:14px;line-height:21.5px;color:var(--grey-text)}
.hero-btn{position:absolute;left:382px;top:192px;width:138px;height:33px;background:var(--red-dark);color:var(--white);font-weight:700;font-size:17px;display:flex;align-items:center;justify-content:center}
.slide-arrow{position:absolute;top:269px;width:22px;height:56px;background:#8f8f8f}
.slide-arrow.prev{left:55px;border-radius:0 28px 28px 0}
.slide-arrow.next{left:752px;width:26px;border-radius:28px 0 0 28px}

/* features */
.feature{position:absolute;top:484px}
.feature h2{font-family:'Cookie',cursive;font-size:25px;color:var(--red);line-height:28px}
.feature p{font-size:10.3px;line-height:13.4px;color:#222;margin-top:2px}
.btn-dark{position:absolute;top:594px;width:88px;height:29px;background:#3a3a3a;border:1px solid #222;color:var(--white);font-size:11.5px;font-weight:700;display:flex;align-items:center;justify-content:center}

/* community banner */
.community{position:absolute;left:260px;top:658px;width:300px;height:63px;background:#fafafa;box-shadow:0 6px 10px -6px rgba(0,0,0,.25),0 -6px 10px -6px rgba(0,0,0,.2);text-align:center}
.community h2{font-family:'Cookie',cursive;font-size:32px;line-height:30px;color:var(--green);margin-top:7px}
.community p{font-family:'Cookie',cursive;font-size:17px;line-height:14px;color:var(--red)}

/* widgets */
.widget-dark{position:absolute;top:749px;height:220px;background:var(--widget-dark);border:2px solid #2c2c2c;color:var(--white)}
.widget-dark h3{font-size:18px;padding:3px 10px;height:27px;border-bottom:1px solid var(--widget-line)}
.recent-list{list-style:none;padding:19px 0 0 23px}
.recent-list li{font-size:9.6px;line-height:12px;color:#e6e6e6;margin-bottom:9.5px}
.follow-btn{position:absolute;right:5px;top:6px;width:44px;height:15px;background:#eee;border-radius:2px;color:#333;font-size:8px;display:flex;align-items:center;justify-content:center}
.tweet{position:absolute;left:2px;width:220px;border-bottom:1px solid var(--widget-line);height:80px}
.avatar{position:absolute;left:8px;top:6px;width:25px;height:25px;background:linear-gradient(#7a8aa0,#4a5566)}
.tweet .who{position:absolute;left:42px;top:5px;font-size:9.5px;line-height:11px}
.tweet .who span{color:#9acd32;display:block}
.tweet .date{position:absolute;left:121px;top:9px;font-size:9.5px}
.tweet p{position:absolute;left:8px;top:37px;width:200px;font-size:9.5px;line-height:12.8px}
.scrollbar{position:absolute;right:4px;top:32px;width:10px;height:160px;background:#e8e8e8}
.tweets-bar{position:absolute;left:2px;bottom:3px;width:229px;height:23px;background:var(--red);color:var(--white);font-size:12.5px;display:flex;align-items:center;justify-content:center}
.fb-box{position:absolute;left:552px;top:749px;width:216px;height:220px;background:var(--white);border:1px solid #b8c3d8}
.fb-head{height:22px;background:#eceff5;border-bottom:1px solid #c4cde0;font-size:9.5px;font-weight:700;color:#333;padding:5px 6px}
.fb-page-thumb{position:absolute;left:6px;top:30px;width:30px;height:30px;background:linear-gradient(#c7b489,#8f7a4f)}
.fb-page-name{position:absolute;left:44px;top:30px;font-size:11px;font-weight:700;color:var(--fb-blue)}
.fb-like{position:absolute;left:44px;top:46px;width:34px;height:14px;border:1px solid #9aa8c6;background:#eef1f7;font-size:8px;color:var(--fb-blue);display:flex;align-items:center;justify-content:center}
.fb-count{position:absolute;left:6px;top:72px;font-size:8px;color:#333}
.fb-faces{position:absolute;left:6px;top:86px;display:grid;grid-template-columns:repeat(5,37px);column-gap:4px;row-gap:6px}
.face{width:37px;height:36px;background:linear-gradient(#a99c8d,#6c625a)}
.face-name{font-size:7px;color:#666;text-align:center;margin-top:2px;white-space:nowrap;overflow:hidden}
.fb-foot{position:absolute;left:6px;bottom:4px;font-size:7.5px;color:#555;display:flex;align-items:center;gap:4px;border-top:1px solid #ddd;width:202px;padding-top:5px}
.fb-foot i{width:8px;height:8px;background:var(--fb-blue);display:block}

/* partner row */
.partner{position:absolute;left:66px;top:1012px;font-size:27px;font-weight:700;color:var(--red-dark);display:flex;align-items:center;gap:12px}
.partner .mark{width:20px;height:20px;background:var(--red-dark)}
.slogan{position:absolute;left:369px;top:1020px;font-family:'Cinzel',Georgia,serif;font-size:22.5px;color:#2f2f2f;letter-spacing:.5px;white-space:nowrap}

/* footer */
.site-footer{position:absolute;left:0;top:1095px;width:858px;height:105px;background:var(--red-dark);border-top:2px solid #7fb0d6;color:var(--white)}
.foot-links{position:absolute;left:57px;top:18px;font-size:10px;line-height:14px}
.foot-lang{position:absolute;left:283px;top:18px;font-size:10px;line-height:14px}
.foot-contact{position:absolute;left:488px;top:16px;font-size:10px;line-height:14px}
.foot-contact .phone{display:flex;align-items:center;gap:8px;font-size:13.5px;margin-bottom:4px}
.dot{display:inline-block;border-radius:50%;background:#3aa0e0}
.socials{position:absolute;left:678px;top:14px;display:flex;gap:7px}
.socials span{width:23px;height:23px;border-radius:50%;background:#e9e9e9;display:block}
.foot-rule{position:absolute;left:100px;top:72px;width:658px;height:1px;background:#8d0e08}
.copyright{position:absolute;left:0;top:86px;width:858px;text-align:center;font-size:9.5px}
</style>
</head>
<body>
<div class="canvas">

  <header class="site-header">
    <div class="brand">
      <div class="brand-name">marisolbrandt</div>
      <div class="brand-tag">THE MARISOL BRANDT TEAM</div>
    </div>
    <div class="work-tab">
      <span class="label">WORK WITH US</span>
      <svg width="16" height="18" viewBox="0 0 16 18" aria-hidden="true"><path d="M3 1l3 0 1 5-2 1c1 3 3 5 5 6l1-2 5 1v3c0 1-1 2-2 2C7 17 0 10 1 3c0-1 1-2 2-2z" fill="#fff"/></svg>
      <span class="phone">555-014-2277</span>
    </div>
    <div class="header-mail">
      <svg width="18" height="12" viewBox="0 0 18 12" aria-hidden="true"><rect width="18" height="12" fill="#f0b400"/><path d="M0 0l9 7 9-7" fill="none" stroke="#c98f00" stroke-width="1.2"/></svg>
      info@marisolbrandt.example
    </div>
  </header>

  <nav class="main-nav">
    <a style="left:128px">HOME</a>
    <a style="left:207px">ABOUT</a>
    <a style="left:295px">BUILDERS</a>
    <a style="left:408px">MORTGAGE INFO</a>
    <a style="left:524px">APPROVAL</a>
    <a style="left:612px">BLOG</a>
    <a style="left:696px">CONTACT</a>
  </nav>

  <div class="hero-backdrop" role="img" aria-label="Soft grey photo of a residential street with buildings and trees"></div>
  <section class="hero-panel">
    <div class="hero-photo" role="img" aria-label="Colourful hot air balloons against a bright blue sky"></div>
    <h1 class="hero-title">EARNING YOUR<br>BUSINESS</h1>
    <p class="hero-text">The Marisol Brandt Team relies on strong systems to deliver an on-time, done-right, friendly experience. Marisol offers mortgages and refinancing services throughout the United States.</p>
    <div class="hero-btn">START HERE</div>
  </section>
  <div class="slide-arrow prev"><svg width="22" height="56" viewBox="0 0 22 56" aria-hidden="true"><path d="M12 22l-6 6 6 6z" fill="#fff"/></svg></div>
  <div class="slide-arrow next"><svg width="26" height="56" viewBox="0 0 26 56" aria-hidden="true"><path d="M14 22l6 6-6 6z" fill="#fff"/></svg></div>

  <section class="feature" style="left:58px;width:258px">
    <h2>Our Credentials</h2>
    <p>Lorem ipsum dolor sit amet, consectetur adipiscing elit. Sed id libero turpis. Nullam sit amet pharetra odio, quis tincidunt mauris. Duis tempus lobortis lectus, vitae porta lorem. Aliquam venenatis diam vitae rhoncus adipiscing. Sed vulputate quis nulla at feugiat. Proin a ultricies lorem.</p>
  </section>
  <section class="feature" style="left:345px;width:182px">
    <h2>Awards</h2>
    <p>Lorem ipsum dolor sit amet, consectetur adipiscing elit. Sed id libero turpis. Nullam sit amet pharetra odio, quis tincidunt mauris. Duis tempus lobortis lectus,</p>
  </section>
  <section class="feature" style="left:568px;width:182px">
    <h2>Recognition</h2>
    <p>Lorem ipsum dolor sit amet, consectetur adipiscing elit. Sed id libero turpis. Nullam sit amet pharetra odio, quis tincidunt mauris. Duis tempus lobortis lectus,</p>
  </section>
  <div class="btn-dark" style="left:53px">READ MORE</div>
  <div class="btn-dark" style="left:341px">READ MORE</div>
  <div class="btn-dark" style="left:565px">READ MORE</div>

  <section class="community">
    <h2>Engaged in our community</h2>
    <p>connect with us</p>
  </section>

  <aside class="widget-dark" style="left:55px;width:238px">
    <h3>Recent Post</h3>
    <ul class="recent-list">
      <li>Happy Friday and Happy End of the Month!</li>
      <li>3 Ways to Use Video to Boost Website</li>
      <li>Traffic! Inside Lending with Marisol Brandt –<br>Update! 3/26/2012</li>
      <li>Congratulations 2nd Year in a Row</li>
      <li>Keystone Funding Cedar Point chosen #1 Best</li>
      <li>Lender by Lakeside Ledger readers!!</li>
      <li>Marisol Brandt's Power Tools</li>
    </ul>
  </aside>

  <aside class="widget-dark" style="left:304px;width:235px">
    <h3>Tweets</h3>
    <div class="follow-btn">Follow</div>
    <div class="tweet" style="top:30px">
      <div class="avatar" role="img" aria-label="Account avatar"></div>
      <div class="who">Northgate Web<span>@northgateweb</span></div>
      <div class="date">26 Jun</div>
      <p>I just wanted to take a moment to say “Thank You” for your business. Have a wonderful weekend. ~The Brandt Team</p>
    </div>
    <div class="tweet" style="top:111px">
      <div class="avatar" role="img" aria-label="Account avatar"></div>
      <div class="who">Northgate Web<span>@northgateweb</span></div>
      <div class="date">26 Jun</div>
      <p>I just wanted to take a moment to say “Thank You” for your business. Have a wonderful weekend. ~The Brandt Team</p>
    </div>
    <div class="scrollbar"></div>
    <div class="tweets-bar">Tweets to @marisolbrandt</div>
  </aside>

  <aside class="fb-box">
    <div class="fb-head">Find us on Facelink</div>
    <div class="fb-page-thumb" role="img" aria-label="Page thumbnail"></div>
    <div class="fb-page-name">Oak Meadow Dairy</div>
    <div class="fb-like">Like</div>
    <div class="fb-count">2,911 people like Oak Meadow Dairy</div>
    <div class="fb-faces">
      <div><div class="face" role="img" aria-label="Follower photo"></div><div class="face-name">Oren</div></div>
      <div><div class="face" role="img" aria-label="Follower photo"></div><div class="face-name">Elin</div></div>
      <div><div class="face" role="img" aria-label="Follower photo"></div><div class="face-name">Tomas Re</div></div>
      <div><div class="face" role="img" aria-label="Follower photo"></div><div class="face-name">Lara</div></div>
      <div><div class="face" role="img" aria-label="Follower photo"></div><div class="face-name">Stefan Dre</div></div>
      <div><div class="face" role="img" aria-label="Follower photo"></div><div class="face-name">Hana</div></div>
      <div><div class="face" role="img" aria-label="Follower photo"></div><div class="face-name">Ayla</div></div>
      <div><div class="face" role="img" aria-label="Follower photo"></div><div class="face-name">Amir</div></div>
      <div><div class="face" role="img" aria-label="Follower photo"></div><div class="face-name">Nico</div></div>
      <div><div class="face" role="img" aria-label="Follower photo"></div><div class="face-name">Ada</div></div>
    </div>
    <div class="fb-foot"><i></i>Facelink social plugin</div>
  </aside>

  <div class="partner"><span>Keystone Funding</span><span class="mark"></span></div>
  <div class="slogan">MORTGAGE WITHOUT OBSTACLES</div>

  <footer class="site-footer">
    <div class="foot-links">Home &nbsp;|&nbsp; About &nbsp;|&nbsp; Mortgage Info &nbsp;|<br>Builders &nbsp;|&nbsp; Approval &nbsp;|&nbsp; Blog</div>
    <div class="foot-lang">Select Language<br>English &nbsp;|&nbsp; French &nbsp;|&nbsp; Portuguese</div>
    <div class="foot-contact">
      <div class="phone"><span class="dot" style="width:16px;height:16px"></span>555-014-2277</div>
      Email : info@marisolbrandt.example
    </div>
    <div class="socials"><span></span><span></span><span></span></div>
    <div class="foot-rule"></div>
    <div class="copyright">© 2013, Al Rights Reserved, Marisol Brandt</div>
  </footer>

</div>
</body>
</html>
```